WP website design (Brantow)

We need a wordpress design for an established auction and real estate company based in Kentucky. The winning design will incorporate a professional color scheme with company logo in a clean layout with specified widgets. The design needs to consider that this will be developed on a responsive theme. Colors will complement the colors in the logo.

Industry/Entity Type

Real Estate

Font styles to use
Sans Serif

Requirements
Must have
• - Navigation:
1) Home 2) Auctions 3) Real Estate Listings 4) Our Services 5) Why Auctions 6) About Us 7) Past Auctions 8) Contact Us

Homeage will have slideshow, please use stock real estate image as the initial slide. Homepage will have this content: "Martin Brantow Auctioneer Real Estate Broker

Buying or selling you can count on Martin Brantow Auctioneer to deliver a quality auction experience. We handle all the details from initial handshake to final payment. We are with you every step of the way giving our sellers the service and results they deserve. You only have one chance for a successful auction. Contact us today to see how our experience and know-how can work for you. We are confident that you will appreciate our higher standard of service."

Footer will have smaller company logo, and attached association logos and this contact info:
Phone: (270) 555-0148
Contacts: Martin Brantow
Email: martinbrantow@mailvex.example
Address: 482 Wexcombe Lane • Bowling Green, KY 42190

Widgets:
1) email sign up 2) Social media (twitter, Youtube - can also be in header 3) News & Events Blog widget 4) testimonials blog 5) Featured Video widget
Nice to have
• Nice to Have:
- demonstrate the drop-down menu styling, e.g. under Auctions
-Upcoming Auctions
-Online Auctions
-Past Auctions

```html
<!DOCTYPE html>
<html lang="en">
<head>
<meta charset="utf-8">
<title>Martin Brantow Auctioneer Real Estate Broker</title>
<link rel="stylesheet" href="https://fonts.googleapis.com/css2?family=Open+Sans:ital,wght@0,400;0,600;0,700;1,400&display=swap">
<style>
:root{
  --blue:#2a5ca8;
  --blue-dark:#1f4c93;
  --yellow:#e9b716;
  --yellow-light:#f3cb2c;
  --text:#555;
  --muted:#888;
  --heading:#5a5a5a;
  --page:#f4f4f4;
  --card:#ffffff;
  --testi:#ececec;
  --footer:#2b2b2b;
  --footer-line:#444;
}
*{margin:0;padding:0;box-sizing:border-box}
html,body{width:1200px;height:2347px;overflow:hidden}
body{font-family:"Open Sans",Arial,sans-serif;color:var(--text);background:var(--page);position:relative}
.abs{position:absolute}

.top-rule{left:0;top:0;width:1200px;height:6px;background:var(--blue)}
.header{left:0;top:6px;width:1200px;height:99px;background:#fff}
.brand{left:131px;top:5px;width:94px;height:79px;display:flex;align-items:center;gap:6px}
.brand-square{width:14px;height:14px;background:var(--yellow);flex:none}
.brand-name{font-weight:700;font-size:15px;line-height:17px;color:var(--blue)}
.search{left:615px;top:39px;width:269px;height:41px;border:1px solid #ddd;background:#fff;font-size:11px;color:#999;padding:12px 14px}
.search-btn{left:884px;top:39px;width:56px;height:41px;background:var(--blue)}
.social{top:40px;width:38px;height:38px;border-radius:50%;border:3px solid #e6e6e6}
.social.tw{left:976px;background:#2aa3e0}
.social.yt{left:1028px;background:#c8201d}

.nav{left:0;top:105px;width:1200px;height:58px;background:linear-gradient(#f2c930,#e2ae10);display:flex;padding-left:131px}
.nav a{display:block;height:58px;line-height:58px;color:#fff;font-size:15px;text-decoration:none;padding:0 16px}
.nav a.active{background:var(--blue);width:104px;text-align:center}

.hero{left:0;top:163px;width:1200px;height:557px;background:linear-gradient(180deg,#b9c6cf 0%,#8a7f6e 45%,#4d3e2e 80%,#3a3026 100%)}
.hero-title{left:131px;top:474px;color:#fff;font-size:70px;line-height:76px;font-weight:400}
.hero-sub{left:131px;top:553px;color:#fff;font-size:60px;line-height:66px}
.hero-arrow{top:411px;width:54px;height:54px;border:2px solid #fff;border-radius:50%}
.hero-arrow.prev{left:17px}.hero-arrow.next{left:1118px}

.section-title{width:1200px;left:0;text-align:center;color:var(--blue);font-weight:700;font-size:34px}
.card{top:829px;width:218px;height:315px;background:var(--card);border:1px solid #ececec}
.card-img{position:absolute;left:17px;top:18px;width:183px;height:181px}
.card-title{position:absolute;left:17px;top:207px;color:var(--yellow);font-size:15px}
.card-text{position:absolute;left:17px;top:229px;width:190px;font-size:11px;line-height:13px;color:#555}
.card-meta{position:absolute;left:17px;top:278px;font-size:13px;color:#999;display:flex;gap:30px;align-items:center}
.card-meta span{display:flex;align-items:center;gap:8px}

.pager{left:406px;top:1186px;display:flex;gap:9px;align-items:center}
.pager span{width:25px;height:25px;border:1px solid #ccc;background:#fff;font-size:10px;color:#555;display:flex;align-items:center;justify-content:center}
.pager span.on{background:#333;color:#fff;border-color:#333}
.pager i{font-style:normal;font-size:12px;color:#555;width:24px;text-align:center}

.divider{left:131px;top:1252px;width:938px;height:8px;background:#e1e1e1}
.col-head{top:1306px;font-size:29px;font-weight:600;color:var(--heading)}
.about-panel{left:443px;top:1306px;width:324px;height:300px;background:linear-gradient(90deg,#e9e9e9,#f7f7f7 12%,#f7f7f7 88%,#e9e9e9)}
.news-thumb{left:131px;width:61px;height:70px}
.news-date{left:203px;font-size:16px;color:var(--blue)}
.small-text{font-size:11.5px;line-height:19px;color:#777}
.link-blue{font-size:14px;font-weight:600;color:var(--blue)}
.btn-yellow{height:28px;background:var(--yellow);color:#fff;font-size:11.5px;font-weight:700;display:flex;align-items:center;justify-content:center}
.video-img{left:800px;top:1356px;width:269px;height:132px}
.play{left:911px;top:1399px;width:46px;height:46px;border-radius:50%;border:3px solid #fff;background:rgba(0,0,0,.35)}

.testi{left:0;top:1646px;width:1200px;height:227px;background:var(--testi)}
.testi-notch{left:583px;top:1646px;width:0;height:0;border-left:17px solid transparent;border-right:17px solid transparent;border-top:15px solid var(--page)}
.testi-title{top:1676px}
.avatar{left:207px;top:1733px;width:92px;height:92px;border-radius:50%;border:5px solid #fff;background:linear-gradient(#d9dee4,#9aa6b4);box-shadow:0 0 4px rgba(0,0,0,.2)}
.quote-mark{font-size:44px;color:#bbb;font-family:Georgia,serif;line-height:40px}
.quote{left:346px;top:1729px;font-style:italic;font-size:13.5px;line-height:23.5px;color:#666;white-space:nowrap}
.quote-name{left:349px;top:1812px;font-size:15px;color:#555}
.t-arrow{top:1744px;width:30px;height:30px;border-radius:50%;background:#dedede}
.t-arrow.prev{left:131px}.t-arrow.next{left:1036px}

.assoc{left:0;top:1873px;width:1200px;height:161px;background:#fff}
.assoc-title{left:131px;top:1931px;font-size:30px;color:#666}
.badge{background:#777}

.news-band{left:0;top:2046px;width:1200px;height:79px;background:var(--blue)}
.news-band-title{left:228px;top:2064px;font-size:32px;font-weight:600;color:#fff}
.field{top:2067px;width:179px;height:37px;background:#fff;font-size:12px;color:#999;padding:10px 14px}
.subscribe{left:968px;top:2067px;width:101px;height:37px;background:var(--yellow);color:#fff;font-size:13px;font-weight:700;display:flex;align-items:center;justify-content:center;border-radius:2px}

.footer{left:0;top:2125px;width:1200px;height:222px;background:var(--footer)}
.foot-brand{left:131px;top:2159px;width:80px;display:flex;gap:5px;align-items:center}
.foot-brand .brand-name{font-size:12px;line-height:14px;color:var(--yellow)}
.foot-sep{top:2155px;width:1px;height:70px;background:var(--footer-line)}
.foot-text{font-size:13px;line-height:24px;color:#fff;white-space:nowrap}
.foot-rule{left:131px;top:2258px;width:938px;height:1px;background:var(--footer-line)}
.foot-links{left:0;width:1200px;top:2276px;display:flex;justify-content:center;gap:0 19px;font-size:13.5px;color:var(--yellow)}
.copy{left:0;width:1200px;top:2313px;text-align:center;font-size:11px;color:#aaa}
</style>
</head>
<body>

<div class="abs top-rule"></div>
<header class="abs header"></header>
<div class="abs brand"><div class="brand-square"></div><div class="brand-name">Martin<br>Brantow</div></div>
<div class="abs search">Enter any keyword...</div>
<div class="abs search-btn">
  <svg width="56" height="41" viewBox="0 0 56 41"><circle cx="25" cy="18" r="7" fill="none" stroke="#fff" stroke-width="3"/><line x1="30" y1="23" x2="36" y2="29" stroke="#fff" stroke-width="4" stroke-linecap="round"/></svg>
</div>
<div class="abs social tw" aria-label="Social profile"></div>
<div class="abs social yt" aria-label="Video channel"></div>

<nav class="abs nav">
  <a class="active">Home</a><a>Auctions</a><a>Real Estate Listings</a><a>Our Services</a><a>Why Auctions</a><a>About Us</a><a>Past Auctions</a><a>Contact Us</a>
</nav>

<section class="abs hero" role="img" aria-label="Slideshow photo of a modern two-storey house with palm trees at dusk"></section>
<div class="abs hero-title">MARTIN BRANTOW</div>
<div class="abs hero-sub">Auctioneer Real Estate Broker</div>
<div class="abs hero-arrow prev"><svg width="50" height="50"><polyline points="29,16 20,25 29,34" fill="none" stroke="#fff" stroke-width="2.5"/></svg></div>
<div class="abs hero-arrow next"><svg width="50" height="50"><polyline points="21,16 30,25 21,34" fill="none" stroke="#fff" stroke-width="2.5"/></svg></div>

<h2 class="abs section-title" style="top:760px">LATEST AUCTIONS</h2>

<article class="abs card" style="left:131px">
  <div class="card-img" role="img" aria-label="Photo of a white modern villa with pool" style="background:linear-gradient(#9fb8cf,#cfd6d8 50%,#6f8a5a)"></div>
  <div class="card-title">At vero eos et accusamus</div>
  <div class="card-text">Lorem ipsum dolor sit amet, conse ctetur adipiscing elita.</div>
  <div class="card-meta"><span><svg width="18" height="18"><path d="M2 2h8l7 7-8 8-7-7z" fill="var(--blue)"/></svg>Bidding</span><span><svg width="16" height="12"><path d="M0 1h3M5 1h11M0 6h3M5 6h11M0 11h3M5 11h11" stroke="#999" stroke-width="2"/></svg>Deatils</span></div>
</article>
<article class="abs card" style="left:374px">
  <div class="card-img" role="img" aria-label="Photo of a white commercial building" style="background:linear-gradient(#6fa6dd,#e4e7ea 55%,#7c7f83)"></div>
  <div class="card-title">At vero eos et accusamus</div>
  <div class="card-text">Lorem ipsum dolor sit amet, conse ctetur adipiscing elita.</div>
  <div class="card-meta"><span><svg width="18" height="18"><path d="M2 2h8l7 7-8 8-7-7z" fill="#aaa"/></svg>Bidding</span><span><svg width="16" height="12"><path d="M0 1h3M5 1h11M0 6h3M5 6h11M0 11h3M5 11h11" stroke="#999" stroke-width="2"/></svg>Deatils</span></div>
</article>
<article class="abs card" style="left:607px">
  <div class="card-img" role="img" aria-label="Photo of a stone family house" style="background:linear-gradient(#8db3dd,#a99e8f 55%,#5e7a45)"></div>
  <div class="card-title">At vero eos et accusamus</div>
  <div class="card-text">Lorem ipsum dolor sit amet, conse ctetur adipiscing elita.</div>
  <div class="card-meta"><span><svg width="18" height="18"><path d="M2 2h8l7 7-8 8-7-7z" fill="#aaa"/></svg>Bidding</span><span><svg width="16" height="12"><path d="M0 1h3M5 1h11M0 6h3M5 6h11M0 11h3M5 11h11" stroke="#999" stroke-width="2"/></svg>Deatils</span></div>
</article>
<article class="abs card" style="left:850px">
  <div class="card-img" role="img" aria-label="Photo of a large white mansion with garden" style="background:linear-gradient(#a9c7e6,#e7e1d6 55%,#6f9150)"></div>
  <div class="card-title">At vero eos et accusamus</div>
  <div class="card-text">Lorem ipsum dolor sit amet, conse ctetur adipiscing elita.</div>
  <div class="card-meta"><span><svg width="18" height="18"><path d="M2 2h8l7 7-8 8-7-7z" fill="#aaa"/></svg>Bidding</span><span><svg width="16" height="12"><path d="M0 1h3M5 1h11M0 6h3M5 6h11M0 11h3M5 11h11" stroke="#999" stroke-width="2"/></svg>Deatils</span></div>
</article>

<div class="abs pager"><span>&lsaquo;</span><span>1</span><span>2</span><span>&lsaquo;</span><span>3</span><span class="on">4</span><i>....</i><span>5</span><span>15</span><span>30</span><span>45</span></div>

<div class="abs divider"></div>

<div class="abs about-panel"></div>
<h3 class="abs col-head" style="left:129px">Latest News &amp; Events</h3>
<h3 class="abs col-head" style="left:477px">About Us</h3>
<h3 class="abs col-head" style="left:799px">Featured Video</h3>

<div class="abs news-thumb" style="top:1366px;background:linear-gradient(#a8c3de,#8c7f6f)" role="img" aria-label="News photo of a house"></div>
<div class="abs news-date" style="top:1359px">25 March ,2014</div>
<p class="abs small-text" style="left:205px;top:1384px;width:225px">At vero eos et accusamus et iusto odjnll! dignissimos ducimus qui blanditiis prae entium voluptatum</p>
<div class="abs news-thumb" style="top:1463px;background:linear-gradient(#b8d0e6,#9a9a84)" role="img" aria-label="News photo of a house"></div>
<div class="abs news-date" style="top:1457px">25 March ,2014</div>
<p class="abs small-text" style="left:205px;top:1482px;width:225px">At vero eos et accusamus et iusto odjnllio dignissimos ducimus qui blanditiis praes entium voluptatum</p>
<div class="abs btn-yellow" style="left:131px;top:1558px;width:94px">More News</div>

<div class="abs link-blue" style="left:477px;top:1362px">Neque porro quisquam est qui dolorem</div>
<p class="abs small-text" style="left:479px;top:1383px;width:275px">At vero eos et accusamus et iusto odjnlllore nfio dignissimos ducimus qui blanditiis praeseque po rro quisquam est qui dolore.</p>
<div class="abs link-blue" style="left:477px;top:1462px">Neque porro quisquam est qui dolorem</div>
<p class="abs small-text" style="left:479px;top:1483px;width:275px">At vero eos et accusamus et iusto odjnlllore nfio dignissimos ducimus qui blanditiis praeseque po rro quisquam est qui dolorem ipsum.</p>
<div class="abs btn-yellow" style="left:479px;top:1558px;width:95px">Read More</div>

<div class="abs video-img" role="img" aria-label="Video still of a suburban house with garage" style="background:linear-gradient(#7fa8d6,#dcd7cc 55%,#7c8a5c)"></div>
<div class="abs play"><svg width="40" height="40"><polygon points="16,12 28,20 16,28" fill="#fff"/></svg></div>
<div class="abs link-blue" style="left:800px;top:1507px">Neque porro quisquam est qui dolorem</div>
<p class="abs small-text" style="left:802px;top:1528px;width:270px">At vero eos et accusamus et iusto odjnlllore nffhho dignissimos ducimus qui blanditiis pxdgxraeseque rro quisquam est qui dolore.</p>

<section class="abs testi"></section>
<div class="abs testi-notch"></div>
<h2 class="abs section-title testi-title" style="font-size:29px;font-weight:600">Testimonials</h2>
<div class="abs t-arrow prev"><svg width="30" height="30"><polyline points="17,9 11,15 17,21" fill="none" stroke="#fff" stroke-width="2"/></svg></div>
<div class="abs t-arrow next"><svg width="30" height="30"><polyline points="13,9 19,15 13,21" fill="none" stroke="#fff" stroke-width="2"/></svg></div>
<div class="abs avatar" role="img" aria-label="Client portrait"></div>
<div class="abs quote-mark" style="left:315px;top:1722px">&ldquo;</div>
<p class="abs quote">Consectetur adipisicing elit, sed do eiusmod tempor incididunt ut labore et dolore magna &nbsp;lorehbfjhb m ipsu<br>Ut enim ad minim veniam, quis nostrud exercitation ullamco laboris nisi ut aliquip ex ea commod<br>Ut enim ad minim veniam, quis nostrud exercitation ullamco laboris nisi ut aliquip ex e</p>
<div class="abs quote-mark" style="left:890px;top:1776px">&rdquo;</div>
<div class="abs quote-name">Jhon smith , city name</div>

<section class="abs assoc"></section>
<div class="abs assoc-title">Our Association</div>
<div class="abs badge" style="left:397px;top:1912px;width:142px;height:96px;border-radius:48px 48px 6px 6px" aria-label="Partner badge"></div>
<div class="abs badge" style="left:564px;top:1915px;width:76px;height:88px;border-radius:4px" aria-label="Partner badge"></div>
<div class="abs badge" style="left:670px;top:1925px;width:150px;height:63px;border-radius:3px" aria-label="Partner badge"></div>
<div class="abs badge" style="left:851px;top:1925px;width:115px;height:68px;border-radius:34px" aria-label="Partner badge"></div>
<div class="abs badge" style="left:995px;top:1917px;width:60px;height:80px;border-radius:3px" aria-label="Partner badge"></div>

<section class="abs news-band"></section>
<svg class="abs" style="left:105px;top:2046px" width="105" height="79" viewBox="0 0 105 79"><path d="M5 40 L52 10 L100 40 L100 79 L5 79 Z" fill="var(--blue-dark)"/><path d="M5 40 L52 62 L100 40" fill="none" stroke="#3b6db8" stroke-width="2"/></svg>
<div class="abs news-band-title">Subscribe Newsletter</div>
<div class="abs field" style="left:577px">Name:</div>
<div class="abs field" style="left:771px">Email Address</div>
<div class="abs subscribe">SUBSCRIBE</div>

<footer class="abs footer"></footer>
<div class="abs foot-brand"><div class="brand-square" style="background:var(--blue)"></div><div class="brand-name">Martin<br>Brantow</div></div>
<div class="abs foot-sep" style="left:260px"></div>
<div class="abs foot-sep" style="left:512px"></div>
<div class="abs foot-sep" style="left:850px"></div>
<div class="abs foot-text" style="left:308px;top:2163px">Contacts: Martin Brantow<br>Phone: (270) 555-0148</div>
<div class="abs foot-text" style="left:570px;top:2163px">Phone: (270) 555-0148<br>Email: martinbrantow@mailvex.example</div>
<div class="abs foot-text" style="left:878px;top:2163px">Address: 482 Wexcombe Lane •<br>Bowling Green, KY 42190</div>
<div class="abs foot-rule"></div>
<div class="abs foot-links"><span>Home</span><span>Auctions</span><span>Real Estate Listings</span><span>Our Services</span><span>Why Auctions</span><span>About Us</span><span>Past Auctions</span><span>Contact Us</span></div>
<div class="abs copy">© 2104 All copyrights Reserved.</div>

</body>
</html>
```